Calura Sunscreen

I need 2 labels for 2 sunscreens.
1: 50SPF Sunscreen suitable for oily and acne prone skin ( elexir from maltese plants that help with excess oil)
2: 50SPF Sunscreen suitable for normal skin made out of essential oils that help to calm down nervous system and stimulate sensation of relaxation.

Not sure if its too much writing on the label ?

Attached is the logo and picture of the bottle, beige tannish color 50ml

I wanted to include : Product of Malta on the label with maltese flag ( i guess smaller than the rest of the text)
I can only use " suitable" and "helps" as it is cosmetic and not medical.

Target Market(s)

Men and women

Industry/Entity Type

Skin care

Requirements
Must have
• Logo, descripción, Calura flag “ product of Malta. Incorporate Calura landscape like in the picture, use Calura clover flower like in picture attached.
Nice to have
• I want the label to be very Calura. Depict the landscape of the picture attached, use clover flower, use the Calura lady logo

```html
<!DOCTYPE html>
<html lang="en">
<head>
<meta charset="UTF-8">
<title>Calura Sunscreen SPF 50+ Label</title>
<link rel="stylesheet" href="https://fonts.googleapis.com/css2?family=Montserrat:wght@300;400;500;700;800&family=Oswald:wght@600;700&display=swap">
<style>
  :root {
    --page: #f0efed;
    --tube: #cfc6b9;
    --tube-light: #d9d1c6;
    --tube-edge: #c3b8aa;
    --crimp: #d4ccc0;
    --crimp-line: #c4baad;
    --band: #c7b69c;
    --band-light: #d6c8b3;
    --ink-dark: #553826;
    --ink-mid: #8b7464;
    --ink-logo: #2b2522;
    --spf: #5b3521;
    --title-fill: #e8e5e2;
    --title-edge: #3e3029;
    --flag-white: #f3f1ef;
    --flag-red: #cf1d25;
    --sky-top: #d9a77a;
    --sky-sun: #f1b95c;
    --sea: #5a7288;
    --cliff: #a5673f;
    --cliff-dark: #7c4a2c;
    --clover-pink: #dc86ad;
    --clover-soft: #e9b4cb;
    --leaf: #6fae62;
  }
  * { margin: 0; padding: 0; box-sizing: border-box; }
  html, body { width: 900px; height: 1200px; overflow: hidden; }
  body { background: var(--page); position: relative; font-family: "Montserrat", sans-serif; }

  .label {
    position: absolute; left: 180px; top: 24px; width: 540px; height: 1152px;
    background: linear-gradient(90deg, var(--tube-edge) 0%, var(--tube-light) 30%, var(--tube-light) 65%, var(--tube) 100%);
    overflow: hidden;
  }
  .crimp {
    position: absolute; left: 0; top: 0; width: 100%; height: 44px;
    background: repeating-linear-gradient(90deg, var(--crimp) 0 3px, var(--crimp-line) 3px 5px);
  }

  .brand-splash {
    position: absolute; left: 78px; top: 64px; width: 380px; height: 280px;
    border-radius: 48% 52% 45% 55% / 55% 45% 55% 45%;
    background: radial-gradient(ellipse at 50% 45%, #f2ece4 0%, #e6dbcd 45%, rgba(222,210,195,0.4) 75%, rgba(222,210,195,0) 100%);
  }
  .brand-mark { position: absolute; left: 0; top: 140px; width: 100%; text-align: center; }
  .brand-mark .dot {
    display: inline-block; width: 14px; height: 14px; border-radius: 50%;
    background: var(--ink-logo); vertical-align: middle; margin-right: 10px;
  }
  .brand-name {
    display: inline-block; vertical-align: middle;
    font-weight: 500; font-size: 50px; color: var(--ink-logo); letter-spacing: 2px;
  }
  .brand-tagline {
    display: block; margin-top: 10px;
    font-weight: 500; font-size: 12px; letter-spacing: 1.2px; color: var(--ink-logo);
  }

  .title-band {
    position: absolute; left: 34px; top: 374px; width: 472px; height: 68px;
    background: linear-gradient(90deg, var(--band) 0%, var(--band-light) 50%, var(--band) 100%);
    text-align: center;
  }
  .title {
    font-weight: 800; font-size: 50px; line-height: 68px; letter-spacing: 5px;
    color: var(--title-fill);
    text-shadow: -1.5px -1.5px 0 var(--title-edge), 1.5px -1.5px 0 var(--title-edge),
                 -1.5px 1.5px 0 var(--title-edge), 1.5px 1.5px 0 var(--title-edge);
  }

  .skin-type {
    position: absolute; left: 95px; top: 462px;
    font-weight: 700; font-size: 28.5px; line-height: 36px; letter-spacing: 1.8px;
    color: var(--ink-dark);
  }
  .benefit {
    position: absolute; left: 97px; top: 540px;
    font-weight: 300; font-size: 25px; line-height: 28px; letter-spacing: 0.6px;
    color: var(--ink-mid);
  }

  .landscape {
    position: absolute; left: 76px; top: 620px; width: 390px; height: 152px;
    background:
      linear-gradient(180deg, var(--sky-top) 0%, var(--sky-sun) 24%, #c8a07e 34%, var(--sea) 46%, #6b8298 64%, var(--cliff) 80%, var(--cliff-dark) 100%);
    box-shadow: 0 1px 2px rgba(60,40,25,0.18);
  }
  .clover {
    position: absolute; left: 76px; top: 784px; width: 254px; height: 268px;
    border-radius: 10px;
    background: linear-gradient(170deg, var(--clover-soft) 0%, var(--clover-pink) 38%, #c98aa2 55%, var(--leaf) 78%, #5c9a52 100%);
    box-shadow: 0 1px 2px rgba(60,40,25,0.15);
  }

  .sun-icon { position: absolute; left: 322px; top: 816px; width: 96px; height: 52px; }
  .spf {
    position: absolute; left: 333px; top: 868px;
    font-family: "Oswald", sans-serif; font-weight: 700; color: var(--spf);
  }
  .spf-label { display: block; font-size: 50px; line-height: 58px; }
  .spf-value { display: block; font-size: 108px; line-height: 104px; margin-left: -2px; letter-spacing: -2px; }
  .spf-value sup { font-size: 44px; vertical-align: top; position: relative; top: 2px; }

  .origin { position: absolute; left: 180px; top: 1064px; width: 184px; text-align: center; }
  .flag { display: flex; width: 134px; height: 42px; margin: 0 auto; box-shadow: 0 0 0 1px rgba(0,0,0,0.08); }
  .flag-white { flex: 1; background: var(--flag-white); }
  .flag-red { flex: 1; background: var(--flag-red); }
  .origin-text { margin-top: 10px; font-weight: 400; font-size: 16px; color: #3a2f29; }
</style>
</head>
<body>
  <main class="label">
    <div class="crimp"></div>

    <div class="brand-splash" role="img" aria-label="Soft beige watercolour splash behind the brand name"></div>
    <div class="brand-mark">
      <span class="dot"></span><span class="brand-name">Calura</span>
      <span class="brand-tagline">NATURAL SKIN COSMETICS</span>
    </div>

    <div class="title-band"><h1 class="title">SUNSCREEN</h1></div>

    <p class="skin-type">SUITABLE FOR OILY<br>&amp; ACNE PRONE SKIN</p>
    <p class="benefit">elexir from maltese plants<br>that help with excess oil</p>

    <div class="landscape" role="img" aria-label="Photograph of a Maltese coastline with cliffs and a bay at sunset"></div>
    <div class="clover" role="img" aria-label="Illustration of pink Maltese clover flowers with green leaves"></div>

    <svg class="sun-icon" viewBox="0 0 96 52" aria-hidden="true">
      <path d="M24 50 A24 24 0 0 1 72 50" fill="none" stroke="#5b3521" stroke-width="7"/>
      <g stroke="#5b3521" stroke-width="2" stroke-linecap="round">
        <line x1="48" y1="14" x2="48" y2="6"/>
        <line x1="38" y1="15" x2="36" y2="8"/>
        <line x1="58" y1="15" x2="60" y2="8"/>
        <line x1="29" y1="20" x2="24" y2="13"/>
        <line x1="67" y1="20" x2="72" y2="13"/>
        <line x1="21" y1="27" x2="14" y2="22"/>
        <line x1="75" y1="27" x2="82" y2="22"/>
        <line x1="16" y1="36" x2="8" y2="33"/>
        <line x1="80" y1="36" x2="88" y2="33"/>
        <line x1="13" y1="46" x2="4" y2="45"/>
        <line x1="83" y1="46" x2="92" y2="45"/>
      </g>
    </svg>
    <div class="spf">
      <span class="spf-label">SPF</span>
      <span class="spf-value">50<sup>+</sup></span>
    </div>

    <div class="origin">
      <div class="flag" role="img" aria-label="Flag of Malta"><span class="flag-white"></span><span class="flag-red"></span></div>
      <p class="origin-text">Product of Malta</p>
    </div>
  </main>
</body>
</html>
```